Tallow Fern Studio business cards

We are a new company based in New Zealand. We Specialize in High end Luxury Residential Architecture.

Every home is bespoke and is designed to each clients individual requirements and needs.

I like to design buildings that inspire people through light and form while offering a high level of comfort and usability.

Lines of sight, proportion and balance are fundamental to the spaces I create.
Updates

August 5th is current deadline - Today's date is the 13th of August.

Target Market(s)

New Zealanders who want a custom individual home design, typically 30-65 year old males and females

Industry/Entity Type

Architecture

Contact Information for Business Card

Director - Derek Holloway
Contact Number - 0274619037
Email - info@tallowfernstudio.co.nz
Webstie - www.tallowfernstudio.co.nz
Social Media - @tallowfernstudio

Font styles to use
Sans Serif

Requirements
Must have
• Logo (Both Sides)
Website
Email
Contact Number
Social Media

Nice to have
• Texture
Should not have
• More than 3 colours - typically I would've thought 2 would be good to match the logo.

```html
<!DOCTYPE html>
<html lang="en">
<head>
<meta charset="utf-8">
<title>Tallow Fern Studio — Business Cards</title>
<link rel="stylesheet" href="https://fonts.googleapis.com/css2?family=Josefin+Sans:wght@300&family=Poppins:wght@300;400;500&display=swap">
<style>
  :root {
    --backdrop: #3b3c40;
    --card: #1e2023;
    --ink: #ffffff;
    --ink-soft: #d9d9d9;
  }
  * { margin: 0; padding: 0; box-sizing: border-box; }
  html, body { width: 1200px; height: 800px; overflow: hidden; }
  body {
    background: var(--backdrop);
    font-family: "Poppins", sans-serif;
    color: var(--ink);
  }
  .canvas {
    width: 1200px; height: 800px;
    display: flex; align-items: center; justify-content: center; gap: 48px;
  }
  .card {
    position: relative;
    width: 525px; height: 300px;
    background: var(--card);
    border-radius: 3px;
    box-shadow: 0 14px 30px rgba(0,0,0,0.35);
  }
  .brand {
    display: flex; flex-direction: column; align-items: center; gap: 16px;
  }
  .brand-mark {
    width: 46px; height: 46px;
    border: 5px solid var(--ink);
    border-radius: 50%;
  }
  .brand-name {
    font-family: "Josefin Sans", sans-serif;
    font-weight: 300;
    font-size: 22px;
    letter-spacing: 0.42em;
    margin-right: -0.42em;
    color: var(--ink);
    white-space: nowrap;
  }
  .card-front .brand {
    position: absolute; left: 0; right: 0; top: 92px;
  }
  .card-back .brand {
    position: absolute; left: 42px; top: 40px; align-items: flex-start;
  }
  .card-back .brand-name { font-size: 19px; }
  .card-back .brand-mark { width: 40px; height: 40px; border-width: 4px; margin-left: 4px; }
  .person {
    position: absolute; left: 42px; bottom: 52px;
    line-height: 1.15;
  }
  .person-name {
    font-weight: 500; font-size: 19px; letter-spacing: 0.02em; text-transform: uppercase;
    white-space: nowrap;
  }
  .person-role {
    font-weight: 300; font-size: 13px; color: var(--ink-soft);
  }
  .divider {
    position: absolute; left: 238px; bottom: 30px;
    width: 1px; height: 100px; background: var(--ink-soft);
  }
  .contacts {
    position: absolute; left: 262px; bottom: 30px;
    list-style: none;
    font-weight: 300; font-size: 12.5px; color: var(--ink-soft);
  }
  .contact { display: flex; align-items: center; gap: 9px; height: 25px; white-space: nowrap; }
  .contact svg { width: 12px; height: 12px; flex: none; }
</style>
</head>
<body>
<main class="canvas">
  <section class="card card-front">
    <div class="brand">
      <span class="brand-mark"></span>
      <span class="brand-name">TALLOW FERN STUDIO</span>
    </div>
  </section>

  <section class="card card-back">
    <div class="brand">
      <span class="brand-mark"></span>
      <span class="brand-name">TALLOW FERN STUDIO</span>
    </div>
    <div class="person">
      <p class="person-name">Derek Holloway</p>
      <p class="person-role">Director</p>
    </div>
    <span class="divider"></span>
    <ul class="contacts">
      <li class="contact">
        <svg viewBox="0 0 24 24" aria-hidden="true"><path fill="#fff" d="M6.6 10.8a15 15 0 0 0 6.6 6.6l2.2-2.2c.3-.3.7-.4 1-.2 1.1.4 2.3.6 3.6.6.6 0 1 .4 1 1V20c0 .6-.4 1-1 1C10.6 21 3 13.4 3 4c0-.6.4-1 1-1h3.5c.6 0 1 .4 1 1 0 1.3.2 2.5.6 3.6.1.3 0 .7-.2 1z"/></svg>
        <span>0274619037</span>
      </li>
      <li class="contact">
        <svg viewBox="0 0 24 24" aria-hidden="true"><rect x="2" y="5" width="20" height="14" fill="#fff"/><path d="M2 5l10 8 10-8" fill="none" stroke="#1e2023" stroke-width="1.8"/></svg>
        <span>info@tallowfernstudio.co.nz</span>
      </li>
      <li class="contact">
        <svg viewBox="0 0 24 24" aria-hidden="true"><circle cx="12" cy="12" r="10" fill="#fff"/><g fill="none" stroke="#1e2023" stroke-width="1.4"><ellipse cx="12" cy="12" rx="4.5" ry="10"/><path d="M2 12h20M4 7h16M4 17h16"/></g></svg>
        <span>www.tallowfernstudio.co.nz</span>
      </li>
      <li class="contact">
        <svg viewBox="0 0 24 24" aria-hidden="true"><circle cx="12" cy="12" r="10" fill="#fff"/></svg>
        <span>@tallowfernstudio</span>
      </li>
    </ul>
  </section>
</main>
</body>
</html>
```